Bolvarin Incorporated

Bolvarin is a business that provides consulting, and manages and supplies trades persons in the construction and heavy industries sector. We build, do maintenance, install machinery, and can manage projects or jobs. Would like or prefer more clean, classic designs. Blacks/greys, but open to almost anything.

Target Market(s)

Industrial/Construction/Manufacturing

Industry/Entity Type

Construction Company

Contact Information for Business Card

Clean, business name on the front, possibly have the details on the back, but open to any ideas.

Logo Text

We currently do not have a slogan, open to ideas

Font styles to use
Serif
Sans Serif

Colors

Designer to choose colors to be used in the design.

Requirements
Should not have
• the oval is not my logo, was just an idea. please don't send 20 designs with the oval

```html
<!DOCTYPE html>
<html lang="en">
<head>
<meta charset="utf-8">
<title>Bolvarin Incorporated – Business Cards</title>
<link href="https://fonts.googleapis.com/css2?family=Roboto+Slab:wght@500&family=Roboto:wght@400;700&display=swap" rel="stylesheet">
<style>
  :root {
    --stage: #2a2a2a;
    --ink: #0d0d0d;
    --paper: #ffffff;
    --arc-grey: #8f8b8b;
    --text-dark: #222222;
    --text-mid: #444444;
    --logo-white: #ffffff;
  }
  * { margin: 0; padding: 0; box-sizing: border-box; }
  html, body { width: 1200px; height: 904px; overflow: hidden; }
  body {
    background: var(--stage);
    position: relative;
    font-family: "Roboto", Arial, sans-serif;
  }
  .card {
    position: absolute;
    width: 560px;
    height: 320px;
    overflow: hidden;
    box-shadow: 0 10px 28px rgba(0,0,0,0.5);
  }
  .card-front {
    left: 120px; top: 110px;
    background: var(--ink);
    display: flex; align-items: center; justify-content: center;
  }
  .wordmark {
    color: var(--logo-white);
    font-family: "Roboto Slab", Georgia, serif;
    font-weight: 500;
    text-align: right;
    line-height: 1;
  }
  .wordmark .name { display: block; font-size: 74px; letter-spacing: 1px; }
  .wordmark .suffix { display: block; font-size: 11px; letter-spacing: 2px; margin-top: 6px; }
  .card-back { left: 500px; top: 480px; background: var(--paper); }
  .card-back .backdrop { position: absolute; inset: 0; }
  .back-wordmark {
    position: absolute; left: 120px; top: 66px;
    width: 290px;
    display: flex; justify-content: center;
    color: var(--ink);
  }
  .back-wordmark .name { font-size: 50px; }
  .back-wordmark .suffix { font-size: 8px; margin-top: 4px; }
  .holder {
    position: absolute; right: 318px; top: 196px;
    text-align: right; color: var(--text-dark);
  }
  .holder .person { font-weight: 700; font-size: 20px; }
  .holder .role { font-size: 15px; color: var(--text-mid); margin-top: 2px; }
  .divider {
    position: absolute; left: 258px; top: 182px;
    width: 1px; height: 68px; background: var(--text-mid);
  }
  .contacts {
    position: absolute; left: 272px; top: 180px;
    list-style: none; color: var(--text-mid); font-size: 15px;
  }
  .contacts li { display: flex; align-items: center; gap: 8px; height: 23px; }
  .contacts svg { width: 13px; height: 13px; fill: var(--text-mid); flex: none; }
  .address {
    position: absolute; right: 60px; bottom: 36px;
    color: var(--text-mid); font-size: 15px;
  }
</style>
</head>
<body>
  <section class="card card-front" aria-label="Card front">
    <div class="wordmark">
      <span class="name">Bolvarin</span>
      <span class="suffix">INCORPORATED</span>
    </div>
  </section>

  <section class="card card-back" aria-label="Card back">
    <svg class="backdrop" viewBox="0 0 560 320" width="560" height="320" aria-hidden="true">
      <rect width="560" height="320" fill="var(--ink)"/>
      <ellipse cx="390" cy="430" rx="414" ry="454" fill="var(--arc-grey)"/>
      <ellipse cx="400" cy="436" rx="404" ry="440" fill="var(--paper)"/>
    </svg>

    <div class="back-wordmark wordmark">
      <div>
        <span class="name">Bolvarin</span>
        <span class="suffix">INCORPORATED</span>
      </div>
    </div>

    <div class="holder">
      <div class="person">Marcus Hale</div>
      <div class="role">Manager</div>
    </div>
    <div class="divider"></div>

    <ul class="contacts">
      <li>
        <svg viewBox="0 0 24 24"><path d="M6.6 10.8a15 15 0 0 0 6.6 6.6l2.2-2.2a1 1 0 0 1 1-.25 11.4 11.4 0 0 0 3.6.57 1 1 0 0 1 1 1V20a1 1 0 0 1-1 1A17 17 0 0 1 3 4a1 1 0 0 1 1-1h3.5a1 1 0 0 1 1 1c0 1.25.2 2.45.57 3.57a1 1 0 0 1-.25 1z"/></svg>
        555-014-2100
      </li>
      <li>
        <svg viewBox="0 0 24 24"><path d="M2 5h20v14H2zm2 2v.5l8 5 8-5V7zm0 2.8V17h16V9.8l-8 5z"/></svg>
        youremail@mailhost.com
      </li>
      <li>
        <svg viewBox="0 0 24 24"><path d="M12 2a10 10 0 1 0 0 20 10 10 0 0 0 0-20zm6.9 6h-3a15 15 0 0 0-1.3-3.9A8 8 0 0 1 18.9 8zM12 4c.8 1.2 1.5 2.5 1.9 4h-3.8c.4-1.5 1.1-2.8 1.9-4zM4.3 14a8 8 0 0 1 0-4h3.4a16 16 0 0 0 0 4zm.8 2h3a15 15 0 0 0 1.3 3.9A8 8 0 0 1 5.1 16zm3-8h-3a8 8 0 0 1 4.3-3.9A15 15 0 0 0 8.1 8zM12 20c-.8-1.2-1.5-2.5-1.9-4h3.8c-.4 1.5-1.1 2.8-1.9 4zm2.3-6H9.7a14 14 0 0 1 0-4h4.6a14 14 0 0 1 0 4zm.3 5.9a15 15 0 0 0 1.3-3.9h3a8 8 0 0 1-4.3 3.9zm1.7-5.9a16 16 0 0 0 0-4h3.4a8 8 0 0 1 0 4z"/></svg>
        www.yourwebsite.com
      </li>
    </ul>

    <div class="address">Your address, city, state, ZIP 0000</div>
  </section>
</body>
</html>
```